Wexbridge Home Services Web Site

Design Web site with 3-4 pages: Home, About Us, Services and Order form / Schedule Appointment (which will likely be link to Tallyo App and Ledgerpine integration.)
Services include: Dryer Vent Cleaning, AC Cleaning, Difficult-to-Reach Light Bulb replacement, Wood Repair and Home Maintenance Plans including Fire Safety Checks and Filter Replacement.

Target Market(s)

Luxury Home Owners, Professionals (Dr's/lawyers) and Seniors

Industry/Entity Type

Home Maintenance

Coding

Coded - Design and coding required

Requirements
Must have
• Tagline - Where Home Maintenance is Effortless

```html
<!DOCTYPE html>
<html lang="en">
<head>
<meta charset="utf-8">
<title>Wexbridge Home Services</title>
<link rel="stylesheet" href="https://fonts.googleapis.com/css2?family=Montserrat:wght@400;500;600;700;800&display=swap">
<style>
:root{
  --gold:#dea628;
  --gold-dark:#c8901a;
  --grey:#6b6b6e;
  --grey-dark:#4f4f52;
  --ink:#4a4a4d;
  --text:#6d6d70;
  --white:#ffffff;
  --cream:#fbf5ea;
}
*{box-sizing:border-box;margin:0;padding:0}
html,body{width:1200px;height:4076px;overflow:hidden}
body{position:relative;background:var(--white);font-family:"Montserrat",sans-serif;color:var(--ink)}
a{color:inherit;text-decoration:none}

/* header */
.site-header{position:absolute;left:0;top:0;width:1200px;height:95px;background:var(--white);z-index:5}
.brand{position:absolute;left:104px;top:30px;display:flex;align-items:center;gap:8px}
.brand-dot{width:16px;height:16px;border-radius:50%;background:var(--gold)}
.brand-name{font-weight:700;font-size:17px;color:var(--gold);letter-spacing:1px}
.main-nav{position:absolute;left:333px;top:37px;display:flex;gap:24px;font-size:11px;font-weight:600;color:var(--ink)}
.main-nav .active{color:var(--gold);position:relative}
.main-nav .active::before{content:"";position:absolute;left:0;right:0;top:-37px;height:3px;background:var(--gold)}
.call{position:absolute;left:720px;top:24px;display:flex;align-items:center;gap:10px}
.call-icon{width:42px;height:42px;border-radius:50%;background:var(--grey);display:flex;align-items:center;justify-content:center}
.call small{display:block;font-size:9px;font-weight:600;color:var(--ink)}
.call strong{display:block;font-size:17px;font-weight:700;color:var(--ink)}
.btn{display:inline-flex;align-items:center;justify-content:center;border-radius:30px;background:var(--gold);color:var(--white);font-weight:700;font-size:10px;letter-spacing:.3px}
.header-btn{position:absolute;left:905px;top:20px;width:190px;height:48px}

/* hero */
.hero-photo{position:absolute;left:0;top:95px;width:1200px;height:760px;background:linear-gradient(100deg,#3d2a18 0%,#6b4a2b 35%,#8a6b4a 60%,#b98a3e 80%,#5b4a3a 100%)}
.hero-title{position:absolute;left:104px;top:242px;font-size:50px;line-height:49px;font-weight:800;color:var(--white)}
.hero-text{position:absolute;left:105px;top:405px;width:360px;font-size:12px;line-height:19px;color:var(--white)}
.hero-btn{position:absolute;left:105px;top:462px;width:274px;height:42px;border:2px solid var(--white);border-radius:24px;color:var(--white);font-size:10.5px;font-weight:700;display:flex;align-items:center;justify-content:center}
.hero-edge{position:absolute;left:0;top:600px}

/* why */
.section-title{position:absolute;left:0;width:1200px;text-align:center;font-weight:700;font-size:27px;line-height:31px;color:var(--grey)}
.feature{position:absolute;top:885px;width:190px;text-align:center}
.feature-icon{width:100px;height:100px;margin:0 auto;display:block}
.feature p{margin-top:14px;font-size:11px;line-height:16px;font-weight:600;color:var(--ink);text-transform:uppercase}

/* committed */
.about-photos{position:absolute;left:193px;top:1093px;width:352px;height:390px;border-radius:176px 176px 0 0;overflow:hidden;display:grid;grid-template-columns:1fr 1fr;grid-template-rows:1fr 1fr;gap:5px;background:var(--white)}
.about-photos div:nth-child(1){background:linear-gradient(135deg,#c9c2b4,#2f4a8a)}
.about-photos div:nth-child(2){background:linear-gradient(135deg,#3b3b3b,#e3c23a 50%,#26428f)}
.about-photos div:nth-child(3){background:linear-gradient(135deg,#2b4794,#1f2f5a)}
.about-photos div:nth-child(4){background:linear-gradient(135deg,#d9d3cb,#3552a3)}
.about-title{position:absolute;left:606px;top:1163px;font-size:26px;line-height:30px;font-weight:700;color:var(--grey)}
.about-text{position:absolute;left:606px;width:420px;font-size:11.5px;line-height:17px;color:var(--text)}
.about-btn{position:absolute;left:608px;top:1399px;width:167px;height:45px}
.play{position:absolute;left:785px;top:1399px;width:45px;height:45px;border-radius:50%;background:var(--grey);display:flex;align-items:center;justify-content:center}

/* services */
.service-card{position:absolute;top:1663px;width:242px;height:367px;background:var(--white);box-shadow:0 10px 30px rgba(0,0,0,.09)}
.service-img{width:242px;height:242px;border-radius:121px 121px 0 0}
.service-card h3{margin:28px 0 0 29px;font-size:12.5px;font-weight:700;color:var(--ink)}
.service-card p{margin:14px 0 0 29px;width:190px;font-size:10.5px;line-height:17px;color:var(--text)}
.service-arrow{position:absolute;right:38px;bottom:-16px;width:32px;height:32px;border-radius:50%;background:var(--gold);display:flex;align-items:center;justify-content:center}
.slider-dots{position:absolute;top:2108px;left:552px;display:flex;gap:6px}
.slider-dots span{width:42px;height:4px;border-radius:2px;background:#d8d8d8}
.slider-dots span.on{background:var(--grey)}

/* booking */
.booking-bg{position:absolute;left:0;top:2190px}
.booking-label{position:absolute;left:192px;top:2368px;font-size:10px;font-weight:700;color:var(--white)}
.booking-title{position:absolute;left:190px;top:2395px;font-size:28px;line-height:32px;font-weight:800;color:var(--white)}
.booking-text{position:absolute;left:192px;top:2472px;width:310px;font-size:11.5px;line-height:17px;color:var(--white)}
.booking-btn{position:absolute;left:192px;top:2560px;width:227px;height:44px}
.device{position:absolute;left:652px;top:2265px;width:238px;height:510px;border-radius:34px;background:linear-gradient(160deg,#3a3a3a,#c99a2c 60%,#2e2e2e);box-shadow:0 30px 40px rgba(0,0,0,.25)}
.device-screen{position:absolute;left:12px;top:12px;right:12px;bottom:12px;border-radius:26px;background:var(--cream)}
.device-name{position:absolute;left:0;right:0;top:230px;text-align:center;font-size:17px;font-weight:700;color:var(--gold)}

/* reviews */
.reviews-word{position:absolute;left:258px;top:3232px;transform:rotate(-90deg);transform-origin:0 0;font-size:84px;font-weight:500;letter-spacing:-2px;color:transparent;-webkit-text-stroke:1.5px var(--grey)}
.bubble{position:absolute;left:378px;top:2890px}
.avatar{position:absolute;left:497px;top:2838px;width:94px;height:94px;border-radius:50%;border:4px solid var(--white);background:linear-gradient(160deg,#b9b0a6,#3b3f4a);box-shadow:0 4px 10px rgba(0,0,0,.15)}
.stars{position:absolute;left:500px;top:2975px;display:flex;gap:3px}
.quote{position:absolute;left:400px;top:3008px;width:285px;text-align:center;font-size:13px;line-height:18.5px;color:var(--white)}
.quote-by{position:absolute;left:400px;top:3100px;width:285px;text-align:center;font-size:12.5px;font-weight:700;color:var(--white)}
.client-title{position:absolute;left:742px;top:2955px;font-size:26px;line-height:30px;font-weight:700;color:var(--grey)}
.client-sub{position:absolute;left:742px;top:3030px;font-size:11px;color:var(--text)}
.client-dots{position:absolute;left:742px;top:3068px;display:flex;gap:8px}
.client-dots span{width:43px;height:4px;border-radius:2px;border:1px solid #bdbdbd}
.client-dots span.on{background:var(--grey);border-color:var(--grey)}

/* cta */
.cta-brand{position:absolute;left:0;top:3325px;width:1200px;display:flex;justify-content:center;align-items:center;gap:12px}
.cta-brand .brand-dot{width:26px;height:26px}
.cta-brand span{font-size:30px;font-weight:700;color:var(--gold);letter-spacing:1px}
.cta-title{position:absolute;left:0;top:3423px;width:1200px;text-align:center;font-size:26px;font-weight:700;color:var(--grey)}
.cta-btn{position:absolute;left:482px;top:3472px;width:182px;height:44px}
.cta-phone{position:absolute;left:672px;top:3472px;width:44px;height:44px;border-radius:50%;background:var(--grey);display:flex;align-items:center;justify-content:center}

/* footer */
.footer-bg{position:absolute;left:0;top:3625px}
.chat{position:absolute;left:1062px;top:3693px;width:66px;height:66px;border-radius:50%;background:var(--gold);display:flex;align-items:center;justify-content:center;box-shadow:0 4px 10px rgba(0,0,0,.15)}
.footer-brand{position:absolute;left:106px;top:3842px;display:flex;align-items:center;gap:9px}
.footer-brand .brand-dot{width:18px;height:18px}
.footer-brand span{font-size:21px;font-weight:700;color:var(--gold)}
.socials{position:absolute;left:140px;top:3914px;display:flex;gap:8px}
.socials span{width:23px;height:23px;border-radius:50%;background:#8d8d90}
.socials span:first-child{background:var(--gold)}
.footer-rule{position:absolute;top:3768px;width:1px;height:170px;background:#8a8a8d}
.footer-col{position:absolute;top:3785px}
.footer-col h4{font-size:17px;font-weight:700;color:var(--white);margin-bottom:18px}
.footer-col li{list-style:none;font-size:10.5px;line-height:22.5px;color:#f0f0f0;display:flex;align-items:center;gap:8px}
.footer-bar{position:absolute;left:0;top:4025px;width:1200px;height:51px;background:var(--grey-dark)}
.copyright{position:absolute;left:0;width:1200px;top:20px;text-align:center;font-size:10.5px;color:#eee}
.legal{position:absolute;left:905px;top:22px;font-size:10.5px;color:#eee}
</style>
</head>
<body>

<header class="site-header">
  <a class="brand" href="#"><span class="brand-dot"></span><span class="brand-name">WEXBRIDGE</span></a>
  <nav class="main-nav">
    <a class="active" href="#">HOME</a><a href="#">ABOUT US</a><a href="#">BLOG</a><a href="#">SERVICES</a><a href="#">CONTACT US</a>
  </nav>
  <div class="call">
    <span class="call-icon"><svg width="18" height="18" viewBox="0 0 24 24"><path fill="#fff" d="M6.6 10.8a15 15 0 0 0 6.6 6.6l2.2-2.2a1 1 0 0 1 1-.25 11.4 11.4 0 0 0 3.6.6 1 1 0 0 1 1 1V20a1 1 0 0 1-1 1A17 17 0 0 1 3 4a1 1 0 0 1 1-1h3.5a1 1 0 0 1 1 1c0 1.25.2 2.45.6 3.6a1 1 0 0 1-.25 1z"/></svg></span>
    <div><small>CALL US:</small><strong>+100-555-0142</strong></div>
  </div>
  <a class="btn header-btn" href="#">SCHEDULE APPOINTMENT</a>
</header>

<section class="hero">
  <div class="hero-photo" role="img" aria-label="Handyman wearing a tool belt with a hammer and work gloves"></div>
  <h1 class="hero-title">WHERE HOME<br>MAINTENANCE<br>IS EFFORTLESS</h1>
  <p class="hero-text">From dryer vent cleaning to home safety checks, we make sure your home runs smoothly, safely, and worry-free.</p>
  <a class="hero-btn" href="#">SCHEDULE YOUR APPOINTMENT TODAY</a>
  <svg class="hero-edge" width="1200" height="260" viewBox="0 0 1200 260">
    <path d="M0 180 Q600 20 1200 140 L1200 260 L0 260Z" fill="#fff"/>
    <path d="M0 180 Q600 20 1200 140" fill="none" stroke="var(--gold)" stroke-width="14"/>
  </svg>
</section>

<section class="why">
  <h2 class="section-title" style="top:820px">WHY CHOOSE US</h2>
  <div class="feature" style="left:210px">
    <svg class="feature-icon" viewBox="0 0 100 100"><circle cx="50" cy="50" r="44" fill="none" stroke="var(--gold)" stroke-width="6"/><circle cx="40" cy="50" r="8" fill="none" stroke="var(--grey)" stroke-width="4"/><path d="M48 50 H68 M62 50 V58" stroke="var(--grey)" stroke-width="4"/></svg>
    <p>Trusted by luxury<br>home owners</p>
  </div>
  <div class="feature" style="left:407px">
    <svg class="feature-icon" viewBox="0 0 100 100"><circle cx="50" cy="50" r="44" fill="none" stroke="var(--gold)" stroke-width="6"/><rect x="34" y="34" width="32" height="32" rx="3" fill="var(--grey)"/><path d="M41 41 L59 59 M59 41 L41 59" stroke="#fff" stroke-width="3"/></svg>
    <p>Tailored services<br>for seniors</p>
  </div>
  <div class="feature" style="left:603px">
    <svg class="feature-icon" viewBox="0 0 100 100"><circle cx="50" cy="50" r="44" fill="none" stroke="var(--gold)" stroke-width="6"/><path d="M50 30 L67 36 V50 C67 58 59 64 50 68 C41 64 33 58 33 50 V36Z" fill="var(--grey)"/><path d="M42 49 L48 55 L59 43" fill="none" stroke="#fff" stroke-width="3"/></svg>
    <p>Licensed, insured,<br>and detail-oriented</p>
  </div>
  <div class="feature" style="left:799px">
    <svg class="feature-icon" viewBox="0 0 100 100"><circle cx="50" cy="50" r="44" fill="none" stroke="var(--gold)" stroke-width="6"/><rect x="32" y="42" width="22" height="26" fill="var(--grey)"/><path d="M63 36 L66 44 L74 44 L68 49 L70 57 L63 52 L56 57 L58 49 L52 44 L60 44Z" fill="var(--grey)"/></svg>
    <p>Professionals’<br>first choice</p>
  </div>
</section>

<section class="about">
  <div class="about-photos" role="img" aria-label="Four-panel collage of a technician in a hard hat servicing home equipment"><div></div><div></div><div></div><div></div></div>
  <h2 class="about-title">COMMITTED TO SIMPLIFYING<br>HOME MAINTENANCE</h2>
  <p class="about-text" style="top:1238px">We understand that maintaining a home can be time-consuming and complex—especially for busy professionals and seniors who value their time. Our mission is simple: to take the hassle out of everyday upkeep while keeping your home safe, efficient, and beautiful.</p>
  <p class="about-text" style="top:1320px">Our team combines experience, professionalism, and care to deliver services tailored to luxury homeowners, doctors, lawyers, and retirees who deserve stress-free maintenance.</p>
  <a class="btn about-btn" href="#">LEARN MORE ABOUT</a>
  <span class="play"><svg width="12" height="12" viewBox="0 0 12 12"><path d="M3 1 L11 6 L3 11Z" fill="#fff"/></svg></span>
</section>

<section class="services">
  <h2 class="section-title" style="top:1570px">OUR PROFESSIONAL HOME<br>MAINTENANCE SERVICES</h2>
  <article class="service-card" style="left:95px">
    <div class="service-img" role="img" aria-label="Gloved hand cleaning a dryer vent" style="background:linear-gradient(150deg,#6b6b6b,#cfcfcf 45%,#e8b522 70%,#f2f2f2)"></div>
    <h3>DRYER VENT CLEANING</h3><p>Prevent fire hazards and improve efficiency with a thorough cleaning of your...</p>
    <span class="service-arrow"><svg width="10" height="10" viewBox="0 0 10 10"><path d="M3 1 L7 5 L3 9" fill="none" stroke="#fff" stroke-width="1.8"/></svg></span>
  </article>
  <article class="service-card" style="left:351px">
    <div class="service-img" role="img" aria-label="Technician in a hard hat checking an air conditioning unit" style="background:linear-gradient(150deg,#3a3a3a,#e0b92c 45%,#2a3f7a 75%,#5a5a5a)"></div>
    <h3>AC CLEANING</h3><p>Breathe fresh air and keep your cooling system running at peak performance.</p>
    <span class="service-arrow"><svg width="10" height="10" viewBox="0 0 10 10"><path d="M3 1 L7 5 L3 9" fill="none" stroke="#fff" stroke-width="1.8"/></svg></span>
  </article>
  <article class="service-card" style="left:606px">
    <div class="service-img" role="img" aria-label="Electrician replacing a high ceiling light bulb" style="background:linear-gradient(160deg,#23344f,#d9b25a 35%,#2d4266 70%,#1e2b40)"></div>
    <h3>LIGHT BULB REPLACEMENT</h3><p>No more struggling with ladders—let us handle those high or tricky spots safely.</p>
    <span class="service-arrow"><svg width="10" height="10" viewBox="0 0 10 10"><path d="M3 1 L7 5 L3 9" fill="none" stroke="#fff" stroke-width="1.8"/></svg></span>
  </article>
  <article class="service-card" style="left:862px">
    <div class="service-img" role="img" aria-label="Carpenter inspecting a wooden board" style="background:linear-gradient(150deg,#bfa780,#c79a4a 40%,#8a5a2c 70%,#3f4a6a)"></div>
    <h3>WOOD REPAIR</h3><p>From minor fixes to maintaining elegant finishes, we preserve your home’s beauty...</p>
    <span class="service-arrow"><svg width="10" height="10" viewBox="0 0 10 10"><path d="M3 1 L7 5 L3 9" fill="none" stroke="#fff" stroke-width="1.8"/></svg></span>
  </article>
  <div class="slider-dots"><span></span><span class="on"></span></div>
</section>

<section class="booking">
  <svg class="booking-bg" width="1200" height="520" viewBox="0 0 1200 520">
    <path d="M0 180 C150 60 400 5 640 5 C900 5 1100 70 1200 130 L1200 520 L0 520Z" fill="var(--grey)"/>
    <path d="M740 6 Q1040 30 1200 130" fill="none" stroke="var(--gold)" stroke-width="16"/>
  </svg>
  <p class="booking-label">SCHEDULE APPOINTMENT</p>
  <h2 class="booking-title">BOOK YOUR SERVICE<br>IN MINUTES</h2>
  <p class="booking-text">Ready to simplify your home maintenance? Use our easy online scheduling form below. Choose your service, select your preferred date, and relax—our team will handle the rest.</p>
  <a class="btn booking-btn" href="#">SCHEDULE MY APPOINTMENT</a>
  <div class="device" role="img" aria-label="Smartphone showing the company booking screen">
    <div class="device-screen"><p class="device-name">WEXBRIDGE</p></div>
  </div>
</section>

<section class="reviews">
  <p class="reviews-word">REVIEWS</p>
  <svg class="bubble" width="330" height="345" viewBox="0 0 330 345">
    <path d="M165 10 A158 158 0 1 1 120 320 C125 335 140 342 150 345 C110 340 70 325 60 300 A158 158 0 0 1 165 10Z" fill="#c99520" transform="translate(4,6)"/>
    <path d="M165 10 A158 158 0 1 1 120 320 C125 335 140 342 150 345 C110 340 70 325 60 300 A158 158 0 0 1 165 10Z" fill="var(--gold)"/>
  </svg>
  <div class="avatar" role="img" aria-label="Client portrait"></div>
  <div class="stars">
    <svg width="80" height="15" viewBox="0 0 80 15"><g fill="#fff"><path id="st" d="M7.5 0 L9.3 5 L14.5 5 L10.3 8.2 L11.9 13.5 L7.5 10.3 L3.1 13.5 L4.7 8.2 L0.5 5 L5.7 5Z"/><use href="#st" x="16"/><use href="#st" x="32"/><use href="#st" x="48"/><use href="#st" x="64"/></g></svg>
  </div>
  <p class="quote">"Finally a maintenance company that actually cares about details. Scheduling was simple and the service was excellent."</p>
  <p class="quote-by">– Local Homeowner</p>
  <h2 class="client-title">WHAT OUR CLIENT<br>SAY ABOUT US</h2>
  <p class="client-sub">Our Happy Customers</p>
  <div class="client-dots"><span></span><span class="on"></span><span></span></div>
</section>

<section class="cta">
  <div class="cta-brand"><span class="brand-dot"></span><span>WEXBRIDGE</span></div>
  <h2 class="cta-title">WHERE HOME MAINTENANCE IS EFFORTLESS</h2>
  <a class="btn cta-btn" href="#">GET IN TOUCH WITH US</a>
  <span class="cta-phone"><svg width="16" height="16" viewBox="0 0 24 24"><path fill="#fff" d="M6.6 10.8a15 15 0 0 0 6.6 6.6l2.2-2.2a1 1 0 0 1 1-.25 11.4 11.4 0 0 0 3.6.6 1 1 0 0 1 1 1V20a1 1 0 0 1-1 1A17 17 0 0 1 3 4a1 1 0 0 1 1-1h3.5a1 1 0 0 1 1 1c0 1.25.2 2.45.6 3.6a1 1 0 0 1-.25 1z"/></svg></span>
</section>

<footer class="site-footer">
  <svg class="footer-bg" width="1200" height="400" viewBox="0 0 1200 400">
    <path d="M0 160 C200 40 450 0 650 0 C900 0 1100 70 1200 150 L1200 400 L0 400Z" fill="var(--grey)"/>
    <path d="M0 150 Q200 40 470 8" fill="none" stroke="var(--gold)" stroke-width="16"/>
  </svg>
  <span class="chat"><svg width="30" height="26" viewBox="0 0 30 26"><path d="M15 1 C23 1 29 6 29 12 C29 18 23 23 15 23 C13 23 11 22.5 9.5 22 L3 25 L5 19.5 C2.5 17.5 1 15 1 12 C1 6 7 1 15 1Z" fill="#fff"/><circle cx="9" cy="12" r="2" fill="var(--gold)"/><circle cx="15" cy="12" r="2" fill="var(--gold)"/><circle cx="21" cy="12" r="2" fill="var(--gold)"/></svg></span>
  <div class="footer-brand"><span class="brand-dot"></span><span>WEXBRIDGE</span></div>
  <div class="socials"><span></span><span></span><span></span><span></span></div>
  <span class="footer-rule" style="left:334px"></span>
  <span class="footer-rule" style="left:553px"></span>
  <span class="footer-rule" style="left:827px"></span>
  <div class="footer-col" style="left:392px">
    <h4>QUICK LINKS</h4>
    <ul><li>Home</li><li>About Us</li><li>Services</li><li>Schedule</li><li>Appointment</li></ul>
  </div>
  <div class="footer-col" style="left:589px">
    <h4>CONTACT</h4>
    <ul>
      <li><svg width="9" height="11" viewBox="0 0 9 11"><path d="M4.5 0 A4.5 4.5 0 0 1 9 4.5 C9 7.5 4.5 11 4.5 11 C4.5 11 0 7.5 0 4.5 A4.5 4.5 0 0 1 4.5 0Z" fill="var(--gold)"/><circle cx="4.5" cy="4.5" r="1.6" fill="var(--grey)"/></svg>Lindenweg 12 40210 Harbourton</li>
      <li><svg width="10" height="10" viewBox="0 0 24 24"><path fill="var(--gold)" d="M6.6 10.8a15 15 0 0 0 6.6 6.6l2.2-2.2a1 1 0 0 1 1-.25 11.4 11.4 0 0 0 3.6.6 1 1 0 0 1 1 1V20a1 1 0 0 1-1 1A17 17 0 0 1 3 4a1 1 0 0 1 1-1h3.5a1 1 0 0 1 1 1c0 1.25.2 2.45.6 3.6a1 1 0 0 1-.25 1z"/></svg>(+100)555-0142</li>
      <li><svg width="11" height="8" viewBox="0 0 11 8"><rect width="11" height="8" rx="1" fill="var(--gold)"/><path d="M0.5 0.5 L5.5 4.5 L10.5 0.5" fill="none" stroke="var(--grey)" stroke-width="1"/></svg>info@wexbridgehome.example</li>
    </ul>
  </div>
  <div class="footer-col" style="left:873px">
    <h4>SERVICES</h4>
    <ul><li>Dryer Vent Cleaning</li><li>AC Cleaning</li><li>Wood Repair</li><li>Home Maintenance Plans</li><li>Light Bulb Replacement</li></ul>
  </div>
  <div class="footer-bar">
    <p class="copyright">Copyright © 2025 Wexbridge Home Services</p>
    <p class="legal">Privacy Policy | Terms &amp; Conditions</p>
  </div>
</footer>

</body>
</html>
```